Thank You Card

I'm looking for a thank you card design using our logo and other graphics. We are an essential business and our employees (Electricians) have done an incredible job staying healthy and safe during the COVID-19 pandemic, I want to send each a thank you card.

```html
<!DOCTYPE html>
<html lang="en">
<head>
<meta charset="utf-8">
<title>Essential Worker Thank You Card</title>
<link href="https://fonts.googleapis.com/css2?family=Montserrat:wght@400;600;800&family=Great+Vibes&display=swap" rel="stylesheet">
<style>
  :root {
    --frame-blue: #0a2aa8;
    --ink-blue: #1a2c8c;
    --accent-red: #e3111c;
    --accent-red-deep: #b80c14;
    --rule-red: #ec6a72;
    --paper: #ffffff;
    --satin-light: #fbfbfb;
    --satin-shade: #e2e2e2;
    --page-bg: #ffffff;
  }
  * { box-sizing: border-box; margin: 0; padding: 0; }
  html, body { width: 1200px; height: 2442px; overflow: hidden; background: var(--page-bg); }
  body { position: relative; font-family: "Montserrat", sans-serif; }

  .spread {
    position: absolute;
    left: 50px;
    width: 1100px;
    height: 394px;
    background: var(--frame-blue);
    padding: 14px;
    display: grid;
    grid-template-columns: 1fr 1fr;
    gap: 14px;
  }
  .spread--outside { top: 780px; }
  .spread--inside { top: 1270px; }

  .panel {
    position: relative;
    background: var(--paper);
    overflow: hidden;
  }
  .panel--satin {
    background:
      radial-gradient(ellipse 70% 40% at 30% 35%, var(--satin-shade) 0%, transparent 70%),
      radial-gradient(ellipse 60% 30% at 75% 75%, var(--satin-shade) 0%, transparent 70%),
      linear-gradient(160deg, var(--satin-light), #efefef 50%, var(--satin-light));
  }
  .panel::after {
    content: "";
    position: absolute;
    inset: 6px;
    border: 1px solid var(--rule-red);
    pointer-events: none;
  }

  .brand-name {
    color: var(--accent-red);
    font-weight: 800;
    text-align: center;
    text-transform: uppercase;
    line-height: 1.05;
    letter-spacing: 0.5px;
  }

  /* back cover */
  .back-cover .brand-name {
    position: absolute;
    left: 0; right: 0; top: 160px;
    font-size: 17px;
  }
  .back-cover .website {
    position: absolute;
    left: 0; right: 0; bottom: 28px;
    text-align: center;
    color: var(--ink-blue);
    font-size: 13px;
  }

  /* front cover */
  .front-cover .brand-name {
    position: absolute;
    left: 0; right: 0; top: 30px;
    font-size: 26px;
  }
  .front-cover .headline {
    position: absolute;
    left: 0; right: 0; top: 110px;
    text-align: center;
    font-family: "Great Vibes", cursive;
    font-weight: 400;
    color: var(--accent-red);
    font-size: 120px;
    line-height: 1;
  }
  .front-cover .occasion {
    position: absolute;
    left: 0; right: 0; bottom: 26px;
    text-align: center;
    color: var(--ink-blue);
    font-weight: 600;
    font-size: 15px;
  }

  /* inside left */
  .hero-panel {
    display: flex;
    flex-direction: column;
    align-items: center;
    justify-content: center;
    gap: 14px;
  }
  .hero-panel .line-top,
  .hero-panel .line-bottom {
    color: var(--ink-blue);
    font-weight: 800;
    text-transform: uppercase;
    line-height: 1;
  }
  .hero-panel .line-top { font-size: 36px; }
  .hero-panel .line-bottom { font-size: 27px; }
  .hero-panel .hero-art {
    width: 300px;
    height: 170px;
    background: radial-gradient(ellipse at 50% 45%, var(--accent-red) 0%, var(--accent-red-deep) 100%);
  }

  /* inside right */
  .message-panel {
    text-align: center;
    padding-top: 46px;
  }
  .message-panel .lead {
    color: var(--ink-blue);
    font-size: 20px;
    line-height: 1.4;
  }
  .message-panel .lead .accent { color: var(--accent-red); display: block; }
  .message-panel .wish {
    margin-top: 36px;
    color: var(--ink-blue);
    font-size: 14px;
    line-height: 1.45;
  }
  .message-panel .wish .accent { color: var(--accent-red); }
  .message-panel .closing {
    margin-top: 36px;
    color: var(--accent-red);
    font-size: 14px;
  }
  .message-panel .signature {
    margin-top: 24px;
    color: #111;
    font-weight: 600;
    font-size: 14px;
  }
</style>
</head>
<body>

  <section class="spread spread--outside" aria-label="Card outside">
    <div class="panel panel--satin back-cover">
      <p class="brand-name">Brightline<br>Service Co.</p>
      <p class="website">www.BrightlineService.com</p>
    </div>
    <div class="panel panel--satin front-cover">
      <p class="brand-name">Brightline<br>Service Co.</p>
      <h1 class="headline">thank you</h1>
      <p class="occasion">Essential Worker 2020</p>
    </div>
  </section>

  <section class="spread spread--inside" aria-label="Card inside">
    <div class="panel hero-panel">
      <p class="line-top">Thank You</p>
      <div class="hero-art" role="img" aria-label="Red star graphic with the word HERO in white display lettering"></div>
      <p class="line-bottom">For All You Do</p>
    </div>
    <div class="panel message-panel">
      <p class="lead">You have done an<br>incredible job providing essential services<span class="accent">during the COVID-19 pandemic.</span></p>
      <p class="wish"><span class="accent">Stay safe and healthy,</span> if there is anything I can do for you<br>please let me know.</p>
      <p class="closing">With gratitude,</p>
      <p class="signature">Daniel Harper</p>
    </div>
  </section>

</body>
</html>
```